Brand new letterhead, business card, email signature etc.

We are a financial company in London, UK. Our website is www.marlowvane.com. We're wanting a complete remodel of the company colours, letter head, business cards, email signatures, etc. Looking to keep the same font for the company name. I have upload a colour palette that we want to work with. We're looking for company letterhead for outgoing letters/ correspondence, letterhead for internal documentation, email signatures, e-letters. etc. Ultimately we will redesign the entire website also. It is important that our clients get a strong, secure, warm, trustworthy, solid feeling and first impression.
Updates

Designs look the same

Target Market(s)

Institutional investors, (ultra) high net worth individuals

Industry/Entity Type

Finance, Invesments banking.

Font styles to use
Other font styles liked:
• Current font is "Champagne & Limousines"

Requirements
Must have
• Must use the colours provided on the PDF uploaded to the portal. The purple = main colour. The red = accent colour.
Nice to have
• Nice to use same font as now for the company name "Quillmoor". Font is "Champagne & Limousines". Nice to have some reference to the old logo flower, but only subtle.
Should not have
• Do not use the colour red from our website. Use the colours provided on the colour palette PDF that I uploaded in the portal.

```html
<!DOCTYPE html>
<html lang="en">
<head>
<meta charset="utf-8">
<title>Quillmoor Letterhead</title>
<link href="https://fonts.googleapis.com/css2?family=Josefin+Sans:wght@300&family=Lato:wght@400;700&family=Kaushan+Script&display=swap" rel="stylesheet">
<style>
  :root {
    --backdrop: #e6e6e7;
    --paper: #ffffff;
    --ink: #241a1d;
    --plum: #2f0d1a;
    --crimson: #c01f34;
    --muted: #4a3f43;
  }
  * { margin: 0; padding: 0; box-sizing: border-box; }
  html, body {
    width: 1200px; height: 874px; overflow: hidden;
    background: var(--backdrop);
  }
  .letterhead {
    position: absolute; left: 305px; top: 20px;
    width: 590px; height: 834px;
    background: var(--paper);
    box-shadow: 0 6px 18px rgba(0,0,0,0.14);
    overflow: hidden;
    font-family: "Lato", sans-serif;
    color: var(--ink);
  }
  .brand {
    position: absolute; left: 48px; top: 56px;
    display: flex; align-items: center; gap: 18px;
  }
  .brand-square {
    width: 70px; height: 70px;
    border: 1px solid var(--plum);
  }
  .brand-name {
    font-family: "Josefin Sans", sans-serif;
    font-weight: 300;
    font-size: 26px;
    letter-spacing: 7px;
    color: var(--plum);
    white-space: nowrap;
  }
  .contact {
    position: absolute; left: 428px; top: 40px;
    padding-left: 14px;
    border-left: 1px solid var(--plum);
    font-family: "Josefin Sans", sans-serif;
    font-weight: 300;
    font-style: normal;
    font-size: 8.5px; line-height: 11px;
    color: var(--muted);
    white-space: nowrap;
  }
  .contact-row { display: flex; align-items: center; gap: 4px; }
  .contact-row svg { width: 7px; height: 7px; fill: var(--plum); }
  .contact-address { margin-top: 3px; padding-left: 11px; }
  .date { position: absolute; left: 58px; top: 180px; font-size: 11px; }
  .recipient { position: absolute; left: 58px; top: 204px; font-size: 11px; line-height: 13.5px; }
  .recipient-company { margin-top: 9px; }
  .salutation {
    position: absolute; left: 58px; top: 308px;
    font-size: 15px; font-weight: 700;
  }
  .body-copy {
    position: absolute; left: 58px; top: 338px; width: 500px;
    font-size: 10.5px; line-height: 13px;
  }
  .body-copy p { margin-bottom: 14px; }
  .closing { position: absolute; left: 58px; top: 612px; font-size: 11px; }
  .signature {
    position: absolute; left: 70px; top: 664px;
    font-family: "Kaushan Script", cursive;
    font-size: 32px; color: #111;
  }
  .footer-bands { position: absolute; left: 0; bottom: 0; width: 590px; height: 44px; }
  .band-accent { fill: var(--crimson); }
  .band-main { fill: var(--plum); }
</style>
</head>
<body>
  <main class="letterhead">
    <header class="brand">
      <div class="brand-square"></div>
      <div class="brand-name">QUILLMOOR</div>
    </header>

    <address class="contact">
      <div class="contact-row">
        <svg viewBox="0 0 10 10"><path d="M2 0.5 L4 2.5 L3 4 Q4.5 6 6 7 L7.5 6 L9.5 8 L8 9.5 Q3 9 0.5 2 Z"/></svg>
        <span>020 7946 0183</span>
      </div>
      <div class="contact-row">
        <svg viewBox="0 0 10 10"><path d="M0 2 H10 V8 H0 Z M0.6 2.4 L5 5.6 L9.4 2.4 V2.8 L5 6.2 L0.6 2.8 Z" fill-rule="evenodd"/></svg>
        <span>info@marlowvane.com</span>
      </div>
      <div class="contact-row">
        <svg viewBox="0 0 10 10"><circle cx="5" cy="5" r="4.5"/></svg>
        <span>www.marlowvane.com</span>
      </div>
      <div class="contact-address">
        Quillmoor Group Limited<br>
        9th Floor 14 Farrow Lane<br>
        London EC2A 7QT
      </div>
    </address>

    <p class="date">January-03-2020</p>

    <div class="recipient">
      <p>Mr. Owen Hale<br>President</p>
      <p class="recipient-company">Brayfield Corporation<br>123 Street Name, Suite# 10<br>City, State, 120023</p>
    </div>

    <p class="salutation">Dear Mr. Owen</p>

    <section class="body-copy">
      <p>Lorem ipsum dolor sit amet, consectetur adipiscing elit, sed do eiusmod tempor incididunt ut labore et dolore magna aliqua. Ut enim ad minim veniam, quis nostrud exercitation ullamco laboris nisi ut aliquip ex ea commodo consequat. Duis aute irure dolor in reprehenderit in voluptate velit esse cillum dolore eu fugiat nulla pariatur.</p>
      <p>Lorem ipsum dolor sit amet, consectetur adipiscing elit, sed do eiusmod tempor incididunt ut labore et dolore magna aliqua. Ut enim ad minim veniam, quis nostrud exercitation ullamco laboris nisi ut aliquip ex ea commodo consequat. Duis aute irure dolor in reprehenderit in voluptate velit esse cillum dolore eu fugiat nulla pariatur.</p>
      <p>Lorem ipsum dolor sit amet, consectetur adipiscing elit, sed do eiusmod tempor incididunt ut labore et dolore magna aliqua. Ut enim ad minim veniam, quis nostrud exercitation ullamco laboris nisi ut aliquip ex ea commodo consequat.</p>
      <p>Excepteur sint occaecat cupidatat non proident, sunt in culpa qui officia deserunt mollit anim id est laborum. re et dolore magnam aliquam quaerat voluptatem.</p>
    </section>

    <p class="closing">Regards</p>
    <p class="signature">Adrian Pell</p>

    <svg class="footer-bands" viewBox="0 0 590 44" preserveAspectRatio="none">
      <polygon class="band-accent" points="0,6 338,6 337,11 0,11"/>
      <polygon class="band-main" points="0,17 336,17 334,44 0,44"/>
      <polygon class="band-accent" points="344,0 590,0 590,44 340,44"/>
    </svg>
  </main>
</body>
</html>
```